SEO Agentur www.tornblau.de - Webseite soll neu designed werden (Start- und Unterseite)
Zielgruppe
Alle Infos sind auf der Seite www.tornblau.de enthalten.
Aufgabenstellung
Die Seite soll neu gestalltet werden. Wir möchten gerne ein wenig professioneller werden. Der Name der Seite zwingt uns allerdings ein gewisses Thema auf.
Die Aufgabe:
Ein professionelleres Design der Startseite und einer Unterseite. Die Programmierung machen wir selbst. Thema Suche und Helden muss bleiben aufgrund der URL.
Mit dem Gewinner würden wir dann auch geren jedes Element der Seite durchgehen und neu gestallten (separater Auftrag).
Das Novaflux Logo ist aufgrund des neuen Films auch gewaltiger und seriöser geworden. Vielleicht kann man daran anknüpfen. Ist aber keine Bedingung nur eine kleine Idee.
Wir werden alle Vorschläge ca. 50 Leuten vorstellen und dann den Vorschlag mit den meisten Stimmen wählen.

```html
<!DOCTYPE html>
<html lang="de">
<head>
<meta charset="utf-8">
<title>Tornblau.de – SEO Agentur</title>
<link href="https://fonts.googleapis.com/css2?family=Open+Sans:wght@300;400;600;700&display=swap" rel="stylesheet">
<style>
:root{
  --red:#e04a52;
  --yellow:#ffe800;
  --blue:#00b4f0;
  --light:#f4f4f4;
  --dark:#2b2b2b;
  --black:#111;
  --text:#222;
  --muted:#777;
  --white:#fff;
}
*{margin:0;padding:0;box-sizing:border-box}
html,body{width:1200px;height:2250px;overflow:hidden}
body{font-family:"Open Sans",Arial,sans-serif;background:var(--light);color:var(--text);position:relative}
.abs{position:absolute}
.header{left:0;top:0;width:1200px;height:89px;background:var(--white)}
.brand{left:240px;top:28px;display:flex;align-items:center;gap:8px;font-weight:700;font-size:15px;color:var(--red)}
.brand-dot{width:26px;height:26px;border-radius:50%;background:var(--red)}
.nav-item{top:0;height:89px;display:flex;flex-direction:column;align-items:center;justify-content:center;font-size:9.5px;color:var(--text);text-align:center;transform:translateX(-50%);white-space:nowrap}
.nav-item svg{margin-top:3px}
.nav-item.active{background:var(--red);color:var(--white);width:105px;transform:none}
.hero{left:0;top:89px;width:1200px;height:413px;background:var(--red);overflow:visible}
.dropdown{left:585px;top:89px;width:105px;height:312px;background:var(--white)}
.dropdown div{height:50px;padding:0 13px;display:flex;align-items:center;font-size:9px;line-height:11px;border-bottom:2px solid var(--red)}
.dropdown div:last-child{border-bottom:none;height:60px}
.hero-title{left:244px;top:420px;color:var(--white);line-height:27px}
.hero-title b{display:block;font-size:26px;font-weight:700}
.hero-title span{display:block;font-size:25px;font-weight:300}
.section-title{left:238px;font-size:28px;font-weight:300;color:var(--red);white-space:nowrap}
.section-title b{font-weight:700}
.rule{left:240px;width:98px;height:2px;background:var(--red)}
.service{top:679px;width:170px;text-align:center;transform:translateX(-50%)}
.service .icon{width:88px;height:88px;border:2px solid var(--text);border-radius:50%;margin:0 auto;display:flex;align-items:center;justify-content:center}
.service h3{margin-top:28px;font-size:19px;font-weight:600;line-height:22px;color:var(--black)}
.service p{margin-top:12px;font-size:9.3px;line-height:11px;color:var(--muted);padding:0 10px}
.btn{display:inline-flex;align-items:center;gap:8px;height:32px;width:81px;justify-content:center;border:2px solid var(--red);border-radius:3px;color:var(--red);font-size:9px;background:transparent}
.service .btn{margin-top:20px}
.btn.light{border-color:var(--white);color:var(--white)}
.band{left:0;top:1068px;width:1200px;height:510px;background:var(--blue)}
.band-text{font-size:11px;line-height:13.5px;color:var(--white);hyphens:auto}
.band-text p+p{margin-top:13px}
.guarantee-text{left:487px;top:1727px;width:460px;font-size:11px;line-height:13.5px;color:var(--text);hyphens:auto}
.guarantee-text p+p{margin-top:13px}
.guarantee-image{left:240px;top:1716px;width:194px;height:192px;background:linear-gradient(160deg,#ffffff 0%,#f1eded 55%,#e9eef3 100%)}
.footer{left:0;top:2008px;width:1200px;height:209px;background:var(--dark);color:var(--white)}
.footer h4{position:absolute;font-size:19px;font-weight:700}
.f-small{font-size:9px;line-height:11px}
.sitemap{top:67px;font-size:9px;line-height:10.8px;color:#9a9a9a;white-space:nowrap}
.sitemap strong{color:#b5b5b5;font-weight:700}
.bottombar{left:0;top:2217px;width:1200px;height:33px;background:var(--black);color:var(--white);font-size:9px}
.social{top:11px;width:12px;height:12px;border-radius:50%;background:var(--white)}
</style>
</head>
<body>

<header class="abs header">
  <div class="abs brand"><span class="brand-dot"></span>Tornblau.de</div>
  <nav>
    <div class="abs nav-item" style="left:464px">Ablauf<svg width="9" height="5"><path d="M1 1l3.5 3L8 1" stroke="#e04a52" fill="none"/></svg></div>
    <div class="abs nav-item" style="left:540px">Ihre Vorteile<svg width="9" height="5"><path d="M1 1l3.5 3L8 1" stroke="#e04a52" fill="none"/></svg></div>
    <div class="abs nav-item active" style="left:585px">Unsere Leistungen<svg width="9" height="5"><path d="M1 1l3.5 3L8 1" stroke="#fff" fill="none"/></svg></div>
    <div class="abs nav-item" style="left:763px">100% Geld-Zurück-Garantie<svg width="9" height="5"><path d="M1 1l3.5 3L8 1" stroke="#e04a52" fill="none"/></svg></div>
    <div class="abs nav-item" style="left:855px">Infos<svg width="9" height="5"><path d="M1 1l3.5 3L8 1" stroke="#e04a52" fill="none"/></svg></div>
    <div class="abs nav-item" style="left:895px">Blog<svg width="9" height="5"><path d="M1 1l3.5 3L8 1" stroke="#e04a52" fill="none"/></svg></div>
    <div class="abs nav-item" style="left:940px">Kontakt<svg width="9" height="5"><path d="M1 1l3.5 3L8 1" stroke="#e04a52" fill="none"/></svg></div>
  </nav>
</header>

<section class="abs hero">
  <svg class="abs" style="left:0;top:0" width="1200" height="470">
    <defs>
      <linearGradient id="photoTone" x1="0" y1="0" x2="1" y2="0">
        <stop offset="0" stop-color="#f3e96a"/>
        <stop offset="0.3" stop-color="#55586a"/>
        <stop offset="0.5" stop-color="#4a68a0"/>
        <stop offset="0.7" stop-color="#55586a"/>
        <stop offset="1" stop-color="#f3e96a"/>
      </linearGradient>
    </defs>
    <polygon points="240,0 960,0 960,85 599,463 240,85" fill="#ffe800"/>
    <rect x="331" y="0" width="532" height="352" fill="url(#photoTone)" role="img" aria-label="Foto: Mann im Anzug öffnet sein Hemd und zeigt ein Heldenkostüm, umgeben von gelben Farbspritzern"/>
  </svg>
</section>

<div class="abs dropdown">
  <div>Suchmaschinen<br>optimierung</div>
  <div>Homepage<br>erstellung</div>
  <div>Suchmaschinen<br>werbung</div>
  <div>Social<br>SEO</div>
  <div>Findora<br>Penalty</div>
  <div>Erklärvideos</div>
</div>

<h1 class="abs hero-title"><b>Ihre Superhelden</b><span>um Gefunden zu werden</span></h1>

<h2 class="abs section-title" style="top:591px">Unsere <b>Leistungen</b></h2>
<div class="abs rule" style="top:634px"></div>

<div class="abs service" style="left:330px">
  <div class="icon"><svg width="54" height="30"><polyline points="3,27 18,15 27,20 50,4" stroke="#222" stroke-width="2.5" fill="none"/><g fill="#222"><circle cx="3" cy="27" r="3"/><circle cx="18" cy="15" r="3"/><circle cx="27" cy="20" r="3"/><circle cx="50" cy="4" r="3"/></g></svg></div>
  <h3>Suchmaschinen<br>optimierung</h3>
  <p>Lorem ipsum dolor sit amet, consetetur sadipscing elitr, sed diam nonumy eirmod tempor invidunt ut labore et dolore magna aliquyam erat, sed diam voluptua. At vero eos et accusam et justo duo dolores et ea</p>
  <span class="btn">Mehr dazu <svg width="6" height="10"><path d="M1 1l4 4-4 4" stroke="#e04a52" fill="none"/></svg></span>
</div>
<div class="abs service" style="left:510px">
  <div class="icon"><span style="font-size:28px;font-weight:700;color:#222">&lt;/&gt;</span></div>
  <h3>Hompage<br>erstellung</h3>
  <p>Lorem ipsum dolor sit amet, consetetur sadipscing elitr, sed diam nonumy eirmod tempor invidunt ut labore et dolore magna aliquyam erat, sed diam voluptua. At vero eos et accusam et justo duo dolores et ea</p>
  <span class="btn">Mehr dazu <svg width="6" height="10"><path d="M1 1l4 4-4 4" stroke="#e04a52" fill="none"/></svg></span>
</div>
<div class="abs service" style="left:690px">
  <div class="icon"><svg width="40" height="34"><rect x="2" y="14" width="5" height="18" fill="#222"/><rect x="9" y="8" width="5" height="24" fill="#222"/><circle cx="22" cy="16" r="7" stroke="#222" stroke-width="3" fill="#fff"/><line x1="27" y1="21" x2="36" y2="31" stroke="#222" stroke-width="4"/></svg></div>
  <h3>Website<br>analysieren</h3>
  <p>Lorem ipsum dolor sit amet, consetetur sadipscing elitr, sed diam nonumy eirmod tempor invidunt ut labore et dolore magna aliquyam erat, sed diam voluptua. At vero eos et accusam et justo duo dolores et ea</p>
  <span class="btn">Mehr dazu <svg width="6" height="10"><path d="M1 1l4 4-4 4" stroke="#e04a52" fill="none"/></svg></span>
</div>
<div class="abs service" style="left:870px">
  <div class="icon"><svg width="36" height="36"><g fill="#222"><rect x="2" y="26" width="4" height="8"/><rect x="8" y="23" width="4" height="11"/><rect x="14" y="20" width="4" height="14"/><rect x="20" y="16" width="4" height="18"/><rect x="26" y="12" width="4" height="22"/><path d="M3 22 Q18 20 25 8 L21 6 L31 1 L31 12 L28 9 Q20 22 3 24z"/></g></svg></div>
  <h3>Social<br>SEO</h3>
  <p>Lorem ipsum dolor sit amet, consetetur sadipscing elitr, sed diam nonumy eirmod tempor invidunt ut labore et dolore magna aliquyam erat, sed diam voluptua. At vero eos et accusam et justo duo dolores et ea</p>
  <span class="btn">Mehr dazu <svg width="6" height="10"><path d="M1 1l4 4-4 4" stroke="#e04a52" fill="none"/></svg></span>
</div>

<section class="abs band">
  <h2 class="abs section-title" style="top:86px;color:var(--white)">Wieso brauchen <b>Sie SEO</b></h2>
  <div class="abs rule" style="top:129px;background:var(--white)"></div>
  <div class="abs band-text" style="left:238px;top:175px;width:350px">
    <p>Durch neue Kunden im Internet wächst Ihr Unternehmen stabil, nachhaltig und kontrolliert. Mit Hilfe unserer Dienstleistung kommen Sie auf die ersten Plätze bei Findora &amp; Co. und bleiben dort auch langfristig.</p>
    <p>Durch unsere Arbeit erhalten Sie mehr Besucher, mehr Kunden und folglich mehr Umsatz! Bereits einer unseren ersten Kunden (ein mittelständischer Werkzeughandel aus Kassel) hat dank unse&shy;rer Hilfe bereits nach 6 Monaten mit seinem Onlineshop eine mo&shy;natliche Umsatzsteigerung von ca. 50%. Diese Umsatzsteigerung ist ausschließlich auf unserer Maßnahmen zurückzuführen.</p>
  </div>
  <div class="abs band-text" style="left:615px;top:174px;width:345px">
    <p>Lassen Sie das Internet nicht links liegen!<br>Fordern Sie jetzt ein <b>kostenloses Angebot</b> für Ihre Optimierung an!</p>
  </div>
  <span class="abs btn light" style="left:876px;top:225px">Mehr dazu <svg width="6" height="10"><path d="M1 1l4 4-4 4" stroke="#fff" fill="none"/></svg></span>
  <div class="abs" style="left:554px;top:353px;width:88px;height:88px;border:2px solid #fff;border-radius:50%;display:flex;align-items:center;justify-content:center">
    <svg width="36" height="36"><g fill="#fff"><rect x="2" y="26" width="4" height="8"/><rect x="8" y="23" width="4" height="11"/><rect x="14" y="20" width="4" height="14"/><rect x="20" y="16" width="4" height="18"/><rect x="26" y="12" width="4" height="22"/><path d="M3 22 Q18 20 25 8 L21 6 L31 1 L31 12 L28 9 Q20 22 3 24z"/></g></svg>
  </div>
</section>

<svg class="abs" style="left:543px;top:1045px" width="112" height="82">
  <polygon points="0,0 112,0 112,23 56,81 0,23" fill="#e04a52"/>
  <path d="M44 43l12 10 12-10" stroke="#fff" stroke-width="2" fill="none"/>
</svg>

<h2 class="abs section-title" style="top:1636px">100% Geld zurück <b>Garantie</b></h2>
<div class="abs rule" style="top:1679px"></div>

<div class="abs guarantee-image" role="img" aria-label="Grafik: Stempel mit der Aufschrift 100% Geld-zurück-Garantie"></div>

<div class="abs guarantee-text">
  <p>Wir von Tornblau.de haben uns auf die Suchmaschinenoptimierung Ihrer Website spezialisiert. Wir helfen Ihnen, dass Sie bei Findora &amp; Co. in den Suchergebnissen ganz vorne gerankt werden. Mit unserer Hilfe steigern Sie Ihre Besucherzahlen, Ihre Kun&shy;denzahlen, Ihr Image und schlussendlich auch Ihre Umsätze. Bei uns erhalten Sie online Marketing aus einer Hand.</p>
  <p>Wir halten was wir versprechen – <b>GARANTIERT!</b> Als einer der wenigen Anbieter geben wir Ihnen eine 100% Geld-Zurück-Garantie, sofern wir Ihre Ziele nicht erreichen.</p>
  <p>Kontaktieren Sie uns und fordern Sie jetzt gleich ein kostenloses Angebot an! Gemein&shy;sam legen wir mit Ihnen zusammen Ihre Ziele fest, damit sich Ihre Website bei Findora &amp; Co. in den Suchergebnissen ganz oben befindet - garantiert.</p>
</div>
<span class="abs btn" style="left:487px;top:1909px">Mehr dazu <svg width="6" height="10"><path d="M1 1l4 4-4 4" stroke="#e04a52" fill="none"/></svg></span>

<footer class="abs footer">
  <h4 style="left:238px;top:24px">Kontakt</h4>
  <svg class="abs" style="left:242px;top:67px" width="14" height="20"><path d="M7 1a6 6 0 0 1 6 6c0 5-6 12-6 12S1 12 1 7a6 6 0 0 1 6-6z" fill="#fff"/><circle cx="7" cy="7" r="2.2" fill="#2b2b2b"/></svg>
  <div class="abs f-small" style="left:272px;top:66px">Tornblau.de GbR<br>Lindenhof 12<br>31840 Brunnstedt</div>
  <svg class="abs" style="left:241px;top:114px" width="18" height="18"><path d="M4 1l3 4-2 2c1 3 3 5 6 6l2-2 4 3-2 3C8 17 1 10 1 3z" fill="#fff"/></svg>
  <div class="abs f-small" style="left:272px;top:114px">Hotline 0512 - 480 915 26<br>Wir warten auf Ihren Anruf</div>
  <div class="abs f-small" style="left:241px;top:162px">Kontakt</div>
  <div class="abs f-small" style="left:295px;top:162px">Impressum</div>

  <h4 style="left:463px;top:24px">Sitemap</h4>
  <div class="abs sitemap" style="left:463px"><strong>Menü</strong><br>Über uns<br>Ihre Vorteile<br>Wie es funktioniert?<br>100% Geld-zurück-Garantie<br>Kontakt<br>Suchmaschinenoptimierung<br>Homepageerstellung<br>Suchmaschinenwerbung<br>Social SEO<br>Blog</div>
  <div class="abs sitemap" style="left:599px"><strong>Suchmaschinenoptimierung</strong><br>SEO Agentur<br>SEO Marketing<br>SEO Umsatz<br>Suchmaschinen-<br>optimierung Agentur<br>SEO Agentur Erfolgsbasiert<br><br><strong>Webseiten</strong><br>Webseiten Erstellung<br>Homepage erstellen lassen</div>
  <div class="abs sitemap" style="left:734px"><strong>Suchmaschinenwerbung</strong><br>Anzeigo Agentur<br>Findora Anzeigo<br>SEA Agentur<br>SEM Agentur<br>Findora Abstrafung<br>Findora Abstrafung<br>Findora Penalty</div>
  <div class="abs sitemap" style="left:865px"><strong>Erklärvideos</strong><br>Erklärvideos<br>Erklärfilme<br>Produktvideos</div>
</footer>

<div class="abs bottombar">
  <div class="abs" style="left:241px;top:11px">Copyright © 2014 Tornblau.de</div>
  <span class="abs social" style="left:857px"></span>
  <span class="abs social" style="left:883px"></span>
  <span class="abs social" style="left:909px"></span>
  <span class="abs social" style="left:936px"></span>
</div>

</body>
</html>
```